Meridale Hair Studio Needs a new appointment business card

We need a new appointment card for our hair salon.

I Dont want bright out there colours.
I would like it to be neat, clean, easy to read. White, Black, with a hint of colour if needed.

We need
-Logo
-Phone number 47260385
-Mobile Number: 0417360528
Address: Shop 3/217 Tarrow Street, Kelby Court, Ashvale 4712

BACK SIDE OF CARD
- Appointment Time & Date (White background so we are able to write on it)
(If you are unable to make your appointment please contact us ASAP 47260385)

I also would like the chatterly and Snapfold logo(Find us on Chatterly)(find us on Snapfold)

Target Market(s)

appointment card simple to read. all information for their next appoint For all our clients male and female

Industry/Entity Type

Hairdresser

Contact Information for Business Card

-Logo
-Phone number 47260385

BACK SIDE OF CARD

Font styles to use
Serif
Sans Serif
Script

Requirements
Must have
• White Back ground on backside with appointment deatils so we are able to write information (like appointment time and date)
Nice to have
• Find us on Chatterly
and
snapfold - meridale_hairstudio
Should not have
• BRIGHT COLOURS

```html
<!DOCTYPE html>
<html lang="en">
<head>
<meta charset="utf-8">
<title>Meridale Hair Studio – Appointment Card</title>
<link href="https://fonts.googleapis.com/css2?family=Montserrat:wght@400;600;700&display=swap" rel="stylesheet">
<style>
  :root {
    --stage: #26272b;
    --card-white: #ffffff;
    --card-black: #000000;
    --ink: #1c1c1c;
    --paper-text: #ffffff;
    --rule: #3a3a3a;
    --motif-light: #d4d4d4;
    --motif-dark-a: #3a3a3a;
    --motif-dark-b: #1a1a1a;
  }
  * { box-sizing: border-box; margin: 0; padding: 0; }
  html, body {
    width: 1200px; height: 900px; overflow: hidden;
    background: var(--stage);
    font-family: "Montserrat", sans-serif;
  }
  .canvas {
    width: 1200px; height: 900px;
    display: flex; align-items: center; justify-content: center; gap: 40px;
  }
  .card {
    position: relative;
    width: 560px; height: 320px;
    overflow: hidden;
  }

  /* Back side – appointment */
  .card--back { background: var(--card-white); color: var(--ink); }
  .appointment-title {
    position: absolute; top: 30px; left: 0; right: 0;
    text-align: center; font-weight: 600; font-size: 17px;
  }
  .appointment-fields {
    position: absolute; top: 68px; left: 36px; right: 36px;
    display: flex; align-items: flex-end; gap: 10px;
    font-weight: 600; font-size: 16px;
  }
  .appointment-fields .blank {
    flex: 1; border-bottom: 1px solid var(--rule); height: 18px;
  }
  .appointment-note {
    position: absolute; top: 104px; left: 0; right: 0;
    text-align: center; font-size: 14.5px; line-height: 1.3;
  }
  .back-motif {
    position: absolute; left: 40px; bottom: 0;
    width: 120px; height: 150px;
    background: linear-gradient(160deg, #ececec, var(--motif-light));
  }
  .social {
    position: absolute; left: 200px; top: 180px;
    font-size: 15px;
  }
  .social-heading { font-weight: 700; font-size: 16px; margin-bottom: 10px; }
  .social-row { display: flex; align-items: center; gap: 10px; margin-bottom: 8px; }
  .social-square { width: 16px; height: 16px; background: var(--ink); border-radius: 3px; }
  .social-circle { width: 16px; height: 16px; border: 2px solid var(--ink); border-radius: 50%; }

  /* Front side – contact */
  .card--front { background: var(--card-black); color: var(--paper-text); }
  .brand-name {
    position: absolute; left: 40px; top: 60px;
    font-weight: 600; font-size: 25px; letter-spacing: 0.04em;
  }
  .brand-mark {
    display: inline-block; width: 12px; height: 12px;
    border: 2px solid var(--paper-text); border-radius: 50%;
    margin-right: 10px; vertical-align: 2px;
  }
  .contact-list {
    position: absolute; left: 40px; top: 140px;
    list-style: none; font-size: 18px;
  }
  .contact-item { display: flex; align-items: flex-start; gap: 12px; margin-bottom: 14px; line-height: 1.3; }
  .contact-icon { width: 20px; height: 22px; flex-shrink: 0; margin-top: 1px; }
  .front-motif {
    position: absolute; right: 40px; top: 20px;
    width: 150px; height: 280px;
    background: linear-gradient(160deg, var(--motif-dark-a), var(--motif-dark-b));
  }
</style>
</head>
<body>
<main class="canvas">

  <section class="card card--back" aria-label="Appointment side">
    <h2 class="appointment-title">Appointment Details</h2>
    <div class="appointment-fields">
      <span>Date</span><span class="blank"></span>
      <span>Time</span><span class="blank"></span>
    </div>
    <p class="appointment-note">If you are unable to make your appointment<br>please contact us ASAP 47260385</p>
    <div class="back-motif" role="img" aria-label="Faint grey open scissors decoration"></div>
    <div class="social">
      <p class="social-heading">Find us on Social Media</p>
      <div class="social-row"><span class="social-square"></span><span>meridalehairstudiokelbycourt</span></div>
      <div class="social-row"><span class="social-circle"></span><span>meridale_hairstudio</span></div>
    </div>
  </section>

  <section class="card card--front" aria-label="Contact side">
    <h1 class="brand-name"><span class="brand-mark"></span>Meridale Hair Studio</h1>
    <ul class="contact-list">
      <li class="contact-item">
        <svg class="contact-icon" viewBox="0 0 24 24" aria-hidden="true"><path fill="#fff" d="M3 8c0-3 4-5 9-5s9 2 9 5v2h-5V8H8v2H3zM6 11h12l2 8H4z"/><circle cx="12" cy="15" r="2.2" fill="#000"/></svg>
        <span>47260385</span>
      </li>
      <li class="contact-item">
        <svg class="contact-icon" viewBox="0 0 24 24" aria-hidden="true"><rect x="6" y="2" width="12" height="20" rx="2" fill="none" stroke="#fff" stroke-width="2"/><line x1="10" y1="18" x2="14" y2="18" stroke="#fff" stroke-width="1.5"/></svg>
        <span>0417360528</span>
      </li>
      <li class="contact-item">
        <svg class="contact-icon" viewBox="0 0 24 24" aria-hidden="true"><path fill="#fff" d="M12 2a7 7 0 0 0-7 7c0 5 7 13 7 13s7-8 7-13a7 7 0 0 0-7-7z"/><circle cx="12" cy="9" r="2.6" fill="#000"/></svg>
        <span>Shop 3/217 Tarrow Street, Kelby<br>Court, Ashvale 4712</span>
      </li>
    </ul>
    <div class="front-motif" role="img" aria-label="Large white open scissors decoration"></div>
  </section>

</main>
</body>
</html>
```